New Website Design for PALVO.org

We are looking for a new website design for PALVO.org. PALVO is a non profit home inspector association based in California. Home Inspectors are people that come out and look at a house before it's purchased to let the buyer know of any defects that may exist.
Our site is based on Joomla so if you'll be able to make a Joomla 3 template as well, please let us know (not required, but a bonus).
We would like to see designs that incorporate royal blue, white and chrome into the site as that's our main business colors.
We would like a place for rotating banners though they don't need to be the same size as the current site.
We would like navigation to be easier to manage with menus only across the top (via drop down menus) where we are going to sort out the items currently on the side. Possibly the front page could have a graphic link to separate portals for Realtors, Home Buyers and Inspectors, but that's just one option.
We would like a good mobile design or something that will scale easily to mobile.
The Find an Inspector feature is important and should stand out. The ZIM PALVOr site
Current home page feels a bit busy. Would like to simplify a bit.

```html
<!DOCTYPE html>
<html lang="en">
<head>
<meta charset="utf-8">
<title>PALVO – Home</title>
<link rel="stylesheet" href="https://fonts.googleapis.com/css2?family=Montserrat:wght@400;600;700&family=Open+Sans:wght@300;400;600;700&family=Nunito+Sans:wght@300;400&display=swap">
<style>
  :root {
    --backdrop: #3d64a6;
    --royal: #1838b4;
    --royal-dark: #12298a;
    --red: #e8282d;
    --white: #ffffff;
    --charcoal: #3a3a3a;
    --charcoal-deep: #2b2b2b;
    --nav: #363636;
    --mist: #efefed;
    --chrome: #a6a6a6;
    --ink: #333333;
    --muted: #555555;
    --footer-text: #d8d8d8;
  }
  * { box-sizing: border-box; margin: 0; padding: 0; }
  html, body { width: 1200px; height: 1000px; overflow: hidden; }
  body { background: var(--backdrop); font-family: "Open Sans", Arial, sans-serif; position: relative; color: var(--ink); }

  .page { position: absolute; left: 209px; top: 23px; width: 779px; height: 960px; background: var(--white); box-shadow: 0 10px 30px rgba(0,0,0,.35); overflow: hidden; }
  .abs { position: absolute; }

  /* header */
  .brand { left: 124px; top: 8px; display: flex; align-items: center; gap: 8px; }
  .brand-dot { width: 30px; height: 30px; border-radius: 50%; background: var(--royal); }
  .brand-name { font-family: "Montserrat", sans-serif; font-weight: 700; font-size: 13px; line-height: 13px; color: #8c8c8c; letter-spacing: .2px; text-transform: uppercase; }
  .search { left: 491px; top: 15px; width: 92px; height: 17px; background: var(--chrome); border-radius: 2px; font-size: 8px; color: #eee; padding: 3px 7px; }
  .search-btn { left: 583px; top: 15px; width: 17px; height: 17px; background: var(--royal); border-radius: 2px; }
  .login { left: 605px; top: 15px; width: 44px; height: 17px; background: var(--royal); border-radius: 2px; color: var(--white); font-size: 7px; font-weight: 700; display: flex; align-items: center; justify-content: center; gap: 3px; }

  /* nav */
  .nav { left: 0; top: 46px; width: 779px; height: 33px; background: var(--nav); border-bottom: 3px solid var(--royal); }
  .nav ul { list-style: none; display: flex; margin-left: 121px; height: 30px; }
  .nav li { font-size: 8.5px; color: var(--white); padding: 0 9.5px; line-height: 30px; font-weight: 600; }
  .nav li.active { background: var(--royal); padding: 0 9px; }

  /* hero */
  .hero { left: 0; top: 81px; width: 779px; height: 239px; background: radial-gradient(circle at 62% 40%, #3c5ed8 0%, #1e3fc0 40%, #1a2f8c 70%), linear-gradient(#58a5f0, #2b56c9); }
  .hero-sky { left: 0; top: 81px; width: 779px; height: 239px; background: linear-gradient(180deg, rgba(110,180,255,.55) 0%, rgba(40,80,200,.1) 45%, rgba(30,50,120,.3) 100%); }
  .hero-title { left: 131px; top: 134px; width: 210px; font-family: "Nunito Sans", sans-serif; font-weight: 300; font-size: 22px; line-height: 27px; color: var(--white); }
  .hero-cta { left: 131px; top: 241px; width: 177px; height: 34px; background: var(--red); color: var(--white); font-family: "Montserrat", sans-serif; font-weight: 600; font-size: 12px; display: flex; align-items: center; justify-content: center; gap: 8px; border-radius: 2px; box-shadow: 0 2px 4px rgba(0,0,0,.3); }
  .hero-arrow { top: 166px; }

  /* welcome */
  .welcome { left: 0; top: 320px; width: 779px; height: 125px; background: var(--mist); text-align: center; }
  .welcome h1 { font-family: "Open Sans", sans-serif; font-weight: 400; font-size: 19px; color: #333; margin-top: 19px; }
  .welcome p { width: 490px; margin: 8px auto 0; font-size: 8.6px; line-height: 11.4px; color: #444; }

  /* portals */
  .portal { top: 470px; width: 142px; text-align: center; }
  .portal-icon { width: 68px; height: 68px; border-radius: 50%; background: var(--royal); margin: 0 auto; display: flex; align-items: center; justify-content: center; }
  .portal h2 { font-family: "Montserrat", sans-serif; font-weight: 700; font-size: 15px; color: #2f2f2f; margin-top: 15px; }
  .portal p { font-size: 7.2px; line-height: 10.1px; color: #555; text-align: justify; margin-top: 9px; }
  .more { display: flex; align-items: center; justify-content: flex-end; gap: 4px; margin-top: 6px; font-size: 6.5px; font-weight: 700; color: #333; }
  .more::before { content: ""; flex: 1; height: 1px; background: #ccc; margin-right: 4px; }
  .more-dot { width: 20px; height: 20px; border-radius: 50%; background: var(--royal); display: flex; align-items: center; justify-content: center; }

  /* search strip */
  .finder { left: 0; top: 714px; width: 779px; height: 62px; background: var(--chrome); border-top: 1px solid #8f8f8f; }
  .finder label { position: absolute; top: 8px; font-size: 8px; color: var(--white); font-weight: 600; }
  .field { position: absolute; top: 21px; height: 22px; background: var(--white); border-radius: 2px; font-size: 8px; color: #444; padding: 6px 8px; }
  .finder-btn { position: absolute; left: 478px; top: 21px; width: 126px; height: 22px; background: var(--red); color: var(--white); font-size: 8px; font-weight: 600; display: flex; align-items: center; justify-content: center; border-radius: 2px; }

  /* footer */
  .footer { left: 0; top: 776px; width: 779px; height: 157px; background: var(--charcoal); color: var(--footer-text); }
  .col { position: absolute; top: 13px; }
  .col h3 { font-size: 11px; font-weight: 400; color: var(--white); margin-bottom: 15px; }
  .col p, .col li { font-size: 7px; line-height: 9.7px; }
  .col ul { list-style: none; }
  .event { margin-bottom: 9px; }
  .event small { display: block; font-size: 4.6px; line-height: 6px; }
  .contact { display: flex; gap: 8px; margin-bottom: 9px; }
  .to-top { left: 656px; top: 907px; width: 24px; height: 24px; background: var(--royal); display: flex; align-items: center; justify-content: center; }
  .bottom { left: 0; top: 933px; width: 779px; height: 27px; background: var(--charcoal-deep); color: #bbb; font-size: 5.5px; }
  .bottom .copy { position: absolute; left: 131px; top: 10px; }
  .bottom .links { position: absolute; left: 511px; top: 10px; display: flex; gap: 8px; }
</style>
</head>
<body>
<div class="page">
  <header>
    <div class="abs brand"><span class="brand-dot"></span><span class="brand-name">Pacific Home<br>Inspection Alliance</span></div>
    <div class="abs search">search...</div>
    <div class="abs search-btn"><svg width="17" height="17" viewBox="0 0 17 17"><circle cx="7.5" cy="7.5" r="3" fill="none" stroke="#fff" stroke-width="1.4"/><line x1="9.7" y1="9.7" x2="12" y2="12" stroke="#fff" stroke-width="1.6"/></svg></div>
    <div class="abs login"><svg width="8" height="8" viewBox="0 0 8 8"><circle cx="4" cy="2.3" r="2" fill="#fff"/><path d="M0 8 Q4 2.5 8 8Z" fill="#fff"/></svg>LOGIN</div>
  </header>

  <nav class="abs nav">
    <ul>
      <li class="active">Home</li><li>Find an Inspector</li><li>Home Buyers &amp; Sellers</li><li>Real Estate Agents</li><li>Inspectors</li><li>ASK PALVO</li><li>Conferences</li>
    </ul>
  </nav>

  <section>
    <div class="abs hero" role="img" aria-label="Banner photo: blurred blue house seen through a magnifying glass showing a lit window"></div>
    <div class="abs hero-sky"></div>
    <h2 class="abs hero-title">We deliver the gold standard in real estate inspections.</h2>
    <div class="abs hero-cta">SEARCH FOR INSPECTOR <svg width="7" height="10" viewBox="0 0 7 10"><path d="M1 1 L5.5 5 L1 9" fill="none" stroke="#fff" stroke-width="2"/></svg></div>
    <svg class="abs hero-arrow" style="left:85px" width="26" height="40" viewBox="0 0 26 40"><path d="M20 3 L5 20 L20 37" fill="none" stroke="rgba(255,255,255,.8)" stroke-width="6"/></svg>
    <svg class="abs hero-arrow" style="left:668px" width="26" height="40" viewBox="0 0 26 40"><path d="M6 3 L21 20 L6 37" fill="none" stroke="rgba(255,255,255,.8)" stroke-width="6"/></svg>
  </section>

  <section class="abs welcome">
    <h1>Welcome to PALVO</h1>
    <p>The Pacific Home Inspection Alliance (PALVO) is a voluntary, nonprofit public-benefit organization of real estate inspectors. Founded in 1976, PALVO provides education, training and support services to its members and the real estate community. PALVO's Code of Ethics and Standards of Practice are recognized by the California Business and Professions Codes and are considered the standard of care by the real estate industry and legal profession in the state.</p>
  </section>

  <section>
    <div class="abs portal" style="left:143px">
      <div class="portal-icon"><svg width="36" height="32" viewBox="0 0 36 32"><path d="M1 4 H7 L11 21 H29 L33 9 H9" fill="none" stroke="#fff" stroke-width="2.5"/><circle cx="13" cy="27" r="2.5" fill="#fff"/><circle cx="27" cy="27" r="2.5" fill="#fff"/><path d="M15 13 L20 8 L25 13 V18 H15Z" fill="#fff"/></svg></div>
      <h2>HOMEBUYERS</h2>
      <p>"Lorem ipsum dolor sit amet, consectetur adipisicing elit, sed do eiusmod tempor incididunt ut labore et dolore magna aliqua. Ut enim ad minim veniam, quis nostrud exercitation ullamco laboris nisi ut aliquip ex ea commodo consequat. Duis aute irure dolor in reprehenderit in voluptate velit esse cillum dolore eu fugiat nulla pariatur.</p>
      <div class="more">READ MORE <span class="more-dot"><svg width="8" height="10" viewBox="0 0 8 10"><path d="M2 1 L6 5 L2 9" fill="none" stroke="#fff" stroke-width="2"/></svg></span></div>
    </div>
    <div class="abs portal" style="left:319px">
      <div class="portal-icon"><svg width="36" height="34" viewBox="0 0 36 34"><circle cx="18" cy="6" r="5" fill="#fff"/><circle cx="8" cy="10" r="4" fill="#fff"/><circle cx="28" cy="10" r="4" fill="#fff"/><rect x="12" y="12" width="12" height="14" rx="3" fill="#fff"/><rect x="3" y="15" width="9" height="12" rx="3" fill="#fff"/><rect x="24" y="15" width="9" height="12" rx="3" fill="#fff"/><rect x="14" y="25" width="8" height="8" fill="#fff"/></svg></div>
      <h2>REALTORS</h2>
      <p>"Lorem ipsum dolor sit amet, consectetur adipisicing elit, sed do eiusmod tempor incididunt ut labore et dolore magna aliqua. Ut enim ad minim veniam, quis nostrud exercitation ullamco laboris nisi ut aliquip ex ea commodo consequat. Duis aute irure dolor in reprehenderit in voluptate velit esse cillum dolore eu fugiat nulla pariatur.</p>
      <div class="more">READ MORE <span class="more-dot"><svg width="8" height="10" viewBox="0 0 8 10"><path d="M2 1 L6 5 L2 9" fill="none" stroke="#fff" stroke-width="2"/></svg></span></div>
    </div>
    <div class="abs portal" style="left:493px">
      <div class="portal-icon"><svg width="38" height="32" viewBox="0 0 38 32"><path d="M2 16 L14 5 L26 16 M6 13 V29 H22 V13" fill="none" stroke="#fff" stroke-width="3"/><circle cx="24" cy="12" r="7" fill="var(--royal)" stroke="#fff" stroke-width="3"/><line x1="29" y1="17" x2="35" y2="23" stroke="#fff" stroke-width="4"/></svg></div>
      <h2>INSPECTORS</h2>
      <p>"Lorem ipsum dolor sit amet, consectetur adipisicing elit, sed do eiusmod tempor incididunt ut labore et dolore magna aliqua. Ut enim ad minim veniam, quis nostrud exercitation ullamco laboris nisi ut aliquip ex ea commodo consequat. Duis aute irure dolor in reprehenderit in voluptate velit esse cillum dolore eu fugiat nulla pariatur.</p>
      <div class="more">READ MORE <span class="more-dot"><svg width="8" height="10" viewBox="0 0 8 10"><path d="M2 1 L6 5 L2 9" fill="none" stroke="#fff" stroke-width="2"/></svg></span></div>
    </div>
  </section>

  <section class="abs finder">
    <label style="left:176px">Distance</label>
    <div class="field" style="left:175px;width:126px"><svg style="position:absolute;right:8px;top:7px" width="10" height="8" viewBox="0 0 10 8"><path d="M1 1 L5 6 L9 1" fill="none" stroke="#333" stroke-width="2"/></svg></div>
    <label style="left:328px">From</label>
    <div class="field" style="left:327px;width:126px">Enter a City or Zip</div>
    <div class="finder-btn">SEARCH FOR INSPECTOR</div>
  </section>

  <footer class="abs footer">
    <div class="col" style="left:122px;width:112px">
      <h3>Who we are</h3>
      <p>Established in 1976, PALVO is a non-profit trade association, with chapters located throughout the state. PALVO is a member-driven, hands-on organization that provides educational programming and on-going opportunities for its members to interact at both local and statewide PALVO meetings and events..</p>
    </div>
    <div class="col" style="left:259px;width:140px">
      <h3>Upcoming Events</h3>
      <ul>
        <li class="event">Fall Conference 2013 - Entire Program<small>09-06-2013 - 09-08-2013</small></li>
        <li class="event">Fall Conference 2013 - Friday Only<small>09-06-2013</small></li>
        <li class="event">Fall Conference 2013 - Guest<small>09-06-2013 - 09-08-2013</small></li>
        <li class="event">Fall Conference 2013 - Saturday Only<small>09-07-2013</small></li>
      </ul>
    </div>
    <div class="col" style="left:410px;width:120px">
      <h3>Latest News</h3>
      <ul><li>NEW - PALVO Vision Statement</li><li style="margin-top:3px">PALVO Regions and Chapters</li><li style="margin-top:3px">PALVO E Learning</li></ul>
    </div>
    <div class="col" style="left:536px;width:140px">
      <h3>Our Contacts</h3>
      <div class="contact"><svg width="12" height="12" viewBox="0 0 12 12"><path d="M0 6 L6 0 L12 6 H10 V12 H7 V8 H5 V12 H2 V6Z" fill="#fff"/></svg><p>2400 Linden Avenue Suite 110<br>Sacramento CA 95800-0000<br>Hours: M-F, 8AM - 5PM</p></div>
      <div class="contact"><svg width="14" height="10" viewBox="0 0 14 10"><path d="M1 3 Q7 -1 13 3 L11 5 L9 3.5 H5 L3 5Z M3 5 H11 V10 H3Z" fill="#fff"/></svg><p>Phone: (800) 555-0142 or<br>(916) 555-0177<br>Fax: (916) 555-0119</p></div>
      <div class="contact"><svg width="12" height="9" viewBox="0 0 12 9"><rect x=".5" y=".5" width="11" height="8" fill="none" stroke="#fff"/><path d="M.5 .5 L6 5 L11.5 .5" fill="none" stroke="#fff"/></svg><p>CEO@PALVO.ORG<br>Webmaster@PALVO.ORG</p></div>
    </div>
  </footer>
  <div class="abs to-top"><svg width="12" height="8" viewBox="0 0 12 8"><path d="M1 7 L6 2 L11 7" fill="none" stroke="#fff" stroke-width="2.5"/></svg></div>
  <div class="abs bottom">
    <span class="copy">Copyright © 2013 PALVO - Pacific Home Inspection Alliance. All Rights Reserved.</span>
    <span class="links"><span>About PALVO</span><span>News</span><span>Privacy/Security/Terms</span></span>
  </div>
</div>
</body>
</html>
```